Nonna's Vellato

I am looking to design a label to be used on a glass jar for packaging a very special spice that has been used in our family for generations. The spice is excellent on meats, burgers, poultry, fish, and more.

The name of the spice is "Nonna's Famous Vellato"

Design should be traditional, with an Italian feel.

Total circumference of the jar is 10"
Height of jar is 4"

Some of the glass should not be covered to reveal color of spice inside.

Target Market(s)

Female 25-75

```html
<!DOCTYPE html>
<html lang="en">
<head>
<meta charset="utf-8">
<title>Nonna's Famous Vellato – Jar Label</title>
<link rel="stylesheet" href="https://fonts.googleapis.com/css2?family=Kaushan+Script&family=Kalam:wght@400;700&family=Delius&display=swap">
<style>
  :root {
    --page: #ffffff;
    --label-red: #c4202f;
    --label-red-bright: #e8212b;
    --gingham-red: #d73a3f;
    --cream: #efe6c6;
    --cream-light: #f7f1dc;
    --tan-text: #f1d9a0;
    --ink: #1e1a17;
    --white: #ffffff;
  }
  html, body {
    margin: 0;
    padding: 0;
    width: 1200px;
    height: 900px;
    overflow: hidden;
    background: var(--page);
  }
  .canvas {
    width: 1200px;
    height: 900px;
    position: relative;
  }
  .label-art {
    display: block;
    width: 1200px;
    height: 900px;
  }
  .band-stripe { fill: var(--label-red); }
  .band-cream { fill: url(#creamWash); }
  .band-bar { fill: var(--label-red); }
  .oval-rim { fill: var(--cream); }
  .oval-gingham { fill: var(--gingham-red); }
  .oval-inner-rim { fill: var(--cream-light); }
  .oval-center { fill: var(--label-red-bright); }
  .placeholder {
    font-family: "Delius", "Kalam", sans-serif;
    font-size: 15px;
    fill: var(--tan-text);
  }
  .brand-owner {
    font-family: "Kaushan Script", cursive;
    font-size: 44px;
    fill: var(--ink);
  }
  .product-name {
    font-family: "Kalam", cursive;
    font-weight: 700;
    font-size: 30px;
    fill: var(--white);
  }
  .tagline {
    font-family: "Delius", "Kalam", sans-serif;
    font-size: 14.5px;
    fill: var(--ink);
  }
</style>
</head>
<body>
<main class="canvas">
  <svg class="label-art" viewBox="0 0 1200 900" xmlns="http://www.w3.org/2000/svg">
    <defs>
      <linearGradient id="creamWash" x1="0" y1="0" x2="0" y2="1">
        <stop offset="0" stop-color="#f3ecd3"/>
        <stop offset="0.5" stop-color="#e9dfbd"/>
        <stop offset="1" stop-color="#f3ecd3"/>
      </linearGradient>
    </defs>

    <g class="wrap-band">
      <rect class="band-cream" x="96" y="402" width="1008" height="112"/>
      <rect class="band-stripe" x="96" y="403" width="1008" height="5"/>
      <rect class="band-stripe" x="96" y="508" width="1008" height="5"/>
    </g>

    <g class="medallion-ring">
      <ellipse class="oval-rim" cx="590" cy="450" rx="162" ry="155"/>
      <ellipse class="oval-gingham" cx="590" cy="452" rx="152" ry="144"
               role="img" aria-label="Red and cream gingham tablecloth pattern"/>
    </g>

    <g class="band-panel">
      <rect class="band-bar" x="216" y="423" width="752" height="65"/>
      <text class="placeholder" x="427" y="461" text-anchor="middle">Text to come</text>
      <text class="placeholder" x="754" y="461" text-anchor="middle">Text to come</text>
    </g>

    <g class="front-medallion">
      <ellipse class="oval-inner-rim" cx="597" cy="461" rx="115" ry="138"/>
      <ellipse class="oval-center" cx="597" cy="461" rx="108" ry="131"/>

      <text class="brand-owner" x="597" y="393" text-anchor="middle">Nonna's</text>
      <text class="product-name" x="600" y="430" text-anchor="middle">Famous</text>
      <text class="product-name" x="604" y="458" text-anchor="middle">Vellato</text>
      <text class="tagline" x="628" y="480" text-anchor="middle">Vellato has</text>
      <text class="tagline" x="592" y="497" text-anchor="middle">been in the family for</text>
      <text class="tagline" x="628" y="514" text-anchor="middle">generations</text>
      <text class="placeholder" x="595" y="544" text-anchor="middle">Text to come</text>
    </g>
  </svg>
</main>
</body>
</html>
```